Letterhead Design Project

We have recently updated our corporate logo and are seeking a new letterhead template.

Attached is the new logo and the old letterhead.

PLEASE DO NOT USE OUR EXISTING WEB SITE FOR INSPIRATION as we are redesigning it.

Target Market(s)

Executives, search professionals, technical and scientific professionals

Industry/Entity Type

Seeking

```html
<!DOCTYPE html>
<html lang="en">
<head>
<meta charset="utf-8">
<title>HelixSeek Letterhead</title>
<link rel="stylesheet" href="https://fonts.googleapis.com/css2?family=Ubuntu:wght@400;500&display=swap">
<style>
  :root {
    --brand-blue: #1a8fc8;
    --rule-light: #9ccbe4;
    --text-grey: #5a6466;
    --paper: #ffffff;
  }
  html, body {
    margin: 0;
    padding: 0;
    width: 900px;
    height: 1200px;
    overflow: hidden;
    background: var(--paper);
  }
  .letterhead {
    position: relative;
    width: 900px;
    height: 1200px;
    font-family: "Ubuntu", sans-serif;
    color: var(--text-grey);
  }
  .brand {
    position: absolute;
    left: 24px;
    top: 32px;
    display: flex;
    align-items: center;
    gap: 14px;
  }
  .brand-dot {
    width: 76px;
    height: 76px;
    border-radius: 50%;
    background: var(--brand-blue);
  }
  .brand-name {
    font-size: 56px;
    font-weight: 500;
    color: var(--brand-blue);
    letter-spacing: -0.5px;
    line-height: 1;
  }
  .website {
    position: absolute;
    right: 14px;
    top: 95px;
    font-size: 20px;
    letter-spacing: 0.2px;
  }
  .rule {
    position: absolute;
    left: 0;
    width: 900px;
  }
  .rule-primary {
    top: 131px;
    height: 4px;
    background: var(--brand-blue);
  }
  .rule-secondary {
    top: 140px;
    height: 3px;
    background: var(--rule-light);
  }
  .contact {
    position: absolute;
    right: 14px;
    bottom: 12px;
    margin: 0;
    text-align: right;
    font-size: 20px;
    line-height: 30px;
    font-style: normal;
  }
</style>
</head>
<body>
  <main class="letterhead">
    <header>
      <div class="brand">
        <span class="brand-dot" aria-hidden="true"></span>
        <span class="brand-name">HelixSeek</span>
      </div>
      <div class="website">www.helixseek.com</div>
      <div class="rule rule-primary"></div>
      <div class="rule rule-secondary"></div>
    </header>
    <footer>
      <address class="contact">
        voice 555.204.3100<br>
        fax 555.204.3110<br>
        2400 North Ridge Road, Suite 140, Eastfield, MA 01234
      </address>
    </footer>
  </main>
</body>
</html>
```